New Alcoholic Spiked Seltzer Line

We need a can design for a line of low calorie alcoholic seltzer. This product is a sparkling water and vodka drink with no sugar added in a slim 12 oz can.

This is a lighter, healthier, alternative to the sugary ready-to-drinks on the market. The product contains only 3 ingredients: Vodka, Water and Natural Flavors. It has only 100 calories but still has 5% alcohol, so you don't need to sacrifice alcohol to cut calories.

This product also does not contain any preservatives.

We want this design to communicate the following objectives to the consumer and in this order:

1. Appetizing product
2.Low calorie
3.Communicate the type of beverage (Spiked Seltzer)

The brand name of the product is VELKA.

The flavor of the product needed to be used for the design is Mango-Orange.

Comparable products are:

www.brisavelfizz.example/
https://www.tarnowbubble.example
https://quellrind.example/

The designs should not infringe or copy the creative directions of the products mentionned above. They are only given so that you can better understand the type of product we are developing.

Target Market(s)

Young Professional women between the ages of 25 and 44

Industry/Entity Type

Product

Colors

Designer to choose colors to be used in the design.

Requirements
Must have
• Design extendibility, meaning it can be adapted for other flavors.
• This is a new category in the market we are targeting, so consumers must easily be able to identify what type of product this is.

```html
<!DOCTYPE html>
<html lang="en">
<head>
<meta charset="utf-8">
<title>VELKA Spiked Seltzer – Mango-Orange Label</title>
<link rel="stylesheet" href="https://fonts.googleapis.com/css2?family=Comfortaa:wght@700&family=Patrick+Hand&family=Crimson+Text:wght@400;600&family=Oswald:wght@500&display=swap">
<style>
  :root {
    --bg: #dfe3e8;
    --label: #f4f5f6;
    --label-edge: #e3e5e8;
    --sky: #1a9ad8;
    --sky-deep: #0f7fc0;
    --mango: #d4621a;
    --mango-light: #e8892c;
    --ink: #1c1c1c;
    --band: #c9ccd0;
    --bubble: #b9bcc0;
  }
  * { margin: 0; padding: 0; box-sizing: border-box; }
  html, body { width: 1200px; height: 1200px; overflow: hidden; }
  body {
    background: var(--bg);
    display: flex;
    align-items: center;
    justify-content: center;
  }
  .can-label {
    position: relative;
    width: 440px;
    height: 1000px;
    background: linear-gradient(90deg, var(--label-edge), var(--label) 30%, var(--label) 70%, var(--label-edge));
    overflow: hidden;
  }
  .label-art { position: absolute; inset: 0; width: 100%; height: 100%; }
  .brand {
    position: absolute;
    top: 330px;
    left: 0; right: 0;
    display: flex;
    align-items: center;
    justify-content: center;
    gap: 18px;
  }
  .brand-dot {
    width: 56px; height: 56px;
    border-radius: 50%;
    background: var(--mango);
  }
  .brand-name {
    font-family: "Comfortaa", sans-serif;
    font-weight: 700;
    font-size: 78px;
    color: var(--mango);
    letter-spacing: 1px;
    text-transform: lowercase;
  }
  .product-type {
    position: absolute;
    top: 700px;
    left: 0; right: 0;
    text-align: center;
    font-family: "Patrick Hand", cursive;
    font-size: 68px;
    color: var(--ink);
    line-height: 1;
  }
  .divider-dots {
    position: absolute;
    top: 800px;
    left: 0; right: 0;
    text-align: center;
    font-family: "Crimson Text", serif;
    font-size: 22px;
    letter-spacing: 8px;
    color: var(--ink);
  }
  .flavor {
    position: absolute;
    top: 842px;
    left: 0; right: 0;
    text-align: center;
    font-family: "Crimson Text", serif;
    font-weight: 600;
    font-size: 28px;
    color: var(--mango);
    letter-spacing: 0.5px;
  }
  .abv {
    position: absolute;
    top: 880px;
    left: 0; right: 0;
    text-align: center;
    font-family: "Crimson Text", serif;
    font-size: 30px;
    color: var(--ink);
  }
  .claim-band {
    position: absolute;
    bottom: 0;
    left: 0; right: 0;
    height: 70px;
    background: var(--band);
    display: flex;
    align-items: center;
    justify-content: center;
    gap: 28px;
    font-family: "Oswald", sans-serif;
    font-weight: 500;
    font-size: 17px;
    color: var(--ink);
  }
</style>
</head>
<body>
  <main class="can-label">
    <svg class="label-art" viewBox="0 0 440 1000" aria-hidden="true">
      <defs>
        <linearGradient id="side-blue" x1="0" y1="0" x2="0" y2="1">
          <stop offset="0" stop-color="var(--sky)"/>
          <stop offset="1" stop-color="var(--sky-deep)"/>
        </linearGradient>
      </defs>
      <path class="side-band side-band--left" d="M0 200 Q30 260 30 520 Q30 760 12 850 L0 850 Z" fill="url(#side-blue)"/>
      <path class="side-band side-band--right" d="M440 170 Q400 300 400 520 Q400 740 440 860 Z" fill="url(#side-blue)"/>
      <g class="bubbles" fill="none" stroke="var(--bubble)" stroke-width="2.5">
        <circle cx="70" cy="110" r="7"/>
        <circle cx="395" cy="110" r="11"/>
        <circle cx="46" cy="515" r="7"/>
        <circle cx="325" cy="665" r="7"/>
        <circle cx="28" cy="885" r="9"/>
        <circle cx="385" cy="887" r="6"/>
      </g>
    </svg>

    <div class="brand">
      <span class="brand-dot"></span>
      <span class="brand-name">velka</span>
    </div>

    <h1 class="product-type">SpikedSeltzer</h1>
    <div class="divider-dots">••••••</div>
    <p class="flavor">MANGO-ORANGE</p>
    <p class="abv">5% Alc./Vol.</p>

    <footer class="claim-band">
      <span>★</span><span>WITH NO ADDED SUGAR</span><span>★</span>
    </footer>
  </main>
</body>
</html>
```